BRAMBLE COFFEE Menu Re-Design (drive-thru coffee shop)

* Keep style of old menu and fonts

* Change to new layout with orange outlines around each product section. I want the orange outlines to look like the orange circle around the "tax not included" on the old menu. I've attached "NEW menu layout 1" for reference.

* Change to new layout, products, sizes, and prices. I attached "Bramble Menu NEW" for reference.

* Change background color of menu from dark blue to light/medium grey

* Change to new logo (my attachment has 3 logos. Use the top/1st logo please).

Let me know if there are any questions about anything or if you need different file types.

Thank you!

Industry/Entity Type

Coffee

Font styles to use
Other font styles liked:
• High Voltage (I've attached the font in the brief.)

Colors
F0912C
F2A743
F7CA91
FBE8D2
FDF5EE

Requirements
Must have
• Grey, Orange and White theme.
Should not have
• The color black

```html
<!DOCTYPE html>
<html lang="en">
<head>
<meta charset="utf-8">
<title>Bramble Coffee Menu</title>
<link href="https://fonts.googleapis.com/css2?family=Bebas+Neue&family=Oswald:wght@500&display=swap" rel="stylesheet">
<style>
  :root{
    --grey-deep:#3a3a3a;
    --grey-mid:#474747;
    --grey-soft:#555555;
    --orange:#ee4f22;
    --white:#f4f4f2;
    --ring:4.5px;
  }
  *{margin:0;padding:0;box-sizing:border-box}
  html,body{width:1200px;height:960px;overflow:hidden;background:var(--grey-deep)}
  .menu{
    position:relative;width:1200px;height:960px;overflow:hidden;
    background:radial-gradient(ellipse at 50% 40%,var(--grey-soft) 0%,var(--grey-mid) 45%,var(--grey-deep) 100%);
    font-family:"Bebas Neue",sans-serif;color:var(--white);
  }
  .bean-pattern{
    position:absolute;left:0;right:0;top:520px;bottom:0;
    background:linear-gradient(to bottom,rgba(90,90,90,0) 0%,rgba(90,90,90,.35) 60%,rgba(95,95,95,.45) 100%);
  }
  .shapes{position:absolute;inset:0}
  .ring{fill:none;stroke:var(--orange);stroke-width:var(--ring)}
  .brush{fill:none;stroke:var(--orange);stroke-width:9;stroke-linecap:round;stroke-dasharray:20 80;stroke-dashoffset:-76}
  .frame{fill:none;stroke:var(--white);stroke-width:2.5}
  .divider{stroke:var(--orange);stroke-width:1.5}
  .rule{stroke:var(--orange);stroke-width:2.5;stroke-linecap:round}

  .label{
    position:absolute;transform:translate(-50%,-50%);
    text-align:center;text-transform:uppercase;white-space:nowrap;
    font-weight:400;line-height:.95;letter-spacing:.01em;
  }
  .label.sm{font-size:26px}
  .label.lg{font-size:62px;line-height:1}
  .label.xl{font-size:52px;line-height:1;letter-spacing:.02em}
  .label.xxl{font-size:56px;line-height:1;letter-spacing:.02em}

  .tax-note{
    font-family:"Oswald",sans-serif;font-weight:500;
    text-transform:none;font-size:30px;line-height:1.2;letter-spacing:-.01em;
  }

  .brand{
    position:absolute;left:166px;top:172px;transform:translate(-50%,-50%);
    display:flex;flex-direction:column;align-items:center;
    color:var(--orange);text-transform:uppercase;line-height:1;
  }
  .brand-mark{width:46px;height:46px;border-radius:50%;background:var(--orange);margin-bottom:10px}
  .brand-name{font-size:76px;letter-spacing:.01em}
  .brand-sub{font-size:32px;letter-spacing:.2em}

  .flavors-title{
    position:absolute;left:318px;top:612px;transform:translate(-50%,-50%);
    font-size:56px;font-weight:400;line-height:1;text-transform:uppercase;letter-spacing:.02em;
  }
</style>
</head>
<body>
<main class="menu">
  <div class="bean-pattern" role="img" aria-label="Faint sketched coffee bean and leaf pattern"></div>

  <svg class="shapes" width="1200" height="960" viewBox="0 0 1200 960" aria-hidden="true">
    <rect class="frame" x="30" y="34" width="1142" height="896"/>
    <rect class="frame" x="43" y="46" width="1115" height="871"/>
    <line class="divider" x1="592" y1="106" x2="592" y2="890"/>

    <ellipse class="ring" cx="483" cy="192" rx="71" ry="74"/>
    <ellipse class="brush" pathLength="100" cx="483" cy="192" rx="71" ry="74"/>

    <g>
      <ellipse class="ring" cx="305" cy="325" rx="118" ry="44"/>
      <ellipse class="brush" pathLength="100" cx="305" cy="325" rx="118" ry="44"/>
      <ellipse class="ring" cx="129" cy="438" rx="57" ry="24"/>
      <ellipse class="brush" pathLength="100" cx="129" cy="438" rx="57" ry="24"/>
      <ellipse class="ring" cx="304" cy="438" rx="97" ry="46"/>
      <ellipse class="brush" pathLength="100" cx="304" cy="438" rx="97" ry="46"/>
      <line class="rule" x1="268" y1="467" x2="340" y2="466"/>
      <ellipse class="ring" cx="483" cy="438" rx="60" ry="28"/>
      <ellipse class="brush" pathLength="100" cx="483" cy="438" rx="60" ry="28"/>
      <ellipse class="ring" cx="192" cy="530" rx="63" ry="32"/>
      <ellipse class="brush" pathLength="100" cx="192" cy="530" rx="63" ry="32"/>
      <ellipse class="ring" cx="423" cy="530" rx="68" ry="32"/>
      <ellipse class="brush" pathLength="100" cx="423" cy="530" rx="68" ry="32"/>

      <path class="ring" d="M235 612 H93 Q83 612 83 622 V702 Q83 712 93 712 H536 Q546 712 546 702 V622 Q546 612 536 612 H402"/>

      <ellipse class="ring" cx="140" cy="776" rx="57" ry="25"/>
      <ellipse class="brush" pathLength="100" cx="140" cy="776" rx="57" ry="25"/>
      <ellipse class="ring" cx="305" cy="778" rx="84" ry="36"/>
      <ellipse class="brush" pathLength="100" cx="305" cy="778" rx="84" ry="36"/>
      <line class="rule" x1="276" y1="802" x2="350" y2="801"/>
      <ellipse class="ring" cx="461" cy="771" rx="57" ry="24"/>
      <ellipse class="brush" pathLength="100" cx="461" cy="771" rx="57" ry="24"/>
      <ellipse class="ring" cx="309" cy="861" rx="68" ry="24"/>
      <ellipse class="brush" pathLength="100" cx="309" cy="861" rx="68" ry="24"/>
    </g>

    <g>
      <ellipse class="ring" cx="880" cy="178" rx="252" ry="58"/>
      <ellipse class="brush" pathLength="100" cx="880" cy="178" rx="252" ry="58"/>
      <line class="rule" x1="738" y1="207" x2="985" y2="206"/>
      <ellipse class="ring" cx="700" cy="305" rx="55" ry="20"/>
      <ellipse class="brush" pathLength="100" cx="700" cy="305" rx="55" ry="20"/>
      <ellipse class="ring" cx="843" cy="305" rx="47" ry="19"/>
      <ellipse class="brush" pathLength="100" cx="843" cy="305" rx="47" ry="19"/>
      <ellipse class="ring" cx="1030" cy="305" rx="100" ry="29"/>
      <ellipse class="brush" pathLength="100" cx="1030" cy="305" rx="100" ry="29"/>

      <ellipse class="ring" cx="880" cy="476" rx="252" ry="85"/>
      <ellipse class="brush" pathLength="100" cx="880" cy="476" rx="252" ry="85"/>
      <line class="rule" x1="742" y1="508" x2="990" y2="507"/>

      <ellipse class="ring" cx="880" cy="675" rx="160" ry="53"/>
      <ellipse class="brush" pathLength="100" cx="880" cy="675" rx="160" ry="53"/>
      <line class="rule" x1="790" y1="703" x2="972" y2="702"/>

      <ellipse class="ring" cx="718" cy="784" rx="81" ry="26"/>
      <ellipse class="brush" pathLength="100" cx="718" cy="784" rx="81" ry="26"/>
      <ellipse class="ring" cx="902" cy="784" rx="81" ry="26"/>
      <ellipse class="brush" pathLength="100" cx="902" cy="784" rx="81" ry="26"/>
      <ellipse class="ring" cx="1053" cy="784" rx="52" ry="19"/>
      <ellipse class="brush" pathLength="100" cx="1053" cy="784" rx="52" ry="19"/>
    </g>
  </svg>

  <header class="brand">
    <span class="brand-mark"></span>
    <span class="brand-name">Bramble</span>
    <span class="brand-sub">Coffee</span>
  </header>

  <p class="label tax-note" style="left:483px;top:193px">Tax Not<br>Included</p>

  <section class="hot-and-cold">
    <p class="label sm" style="left:305px;top:331px">Cold Brew - Nitro<br>Cold Brew</p>
    <p class="label sm" style="left:129px;top:440px">Espresso</p>
    <p class="label lg" style="left:304px;top:440px">Coffee</p>
    <p class="label sm" style="left:483px;top:440px">Drip Coffee</p>
    <p class="label sm" style="left:192px;top:532px">Frozen<br>Espresso</p>
    <p class="label sm" style="left:423px;top:533px">Dairy Free<br>Add-On's</p>
  </section>

  <h2 class="flavors-title">Flavors</h2>

  <section class="teas">
    <p class="label sm" style="left:142px;top:790px">Chai</p>
    <p class="label lg" style="left:308px;top:778px">Tea</p>
    <p class="label sm" style="left:461px;top:773px">Hot Tea</p>
    <p class="label sm" style="left:307px;top:863px">Iced Tea</p>
  </section>

  <section class="energy">
    <p class="label xl" style="left:880px;top:178px">Bramble Energy Soda's</p>
    <p class="label sm" style="left:700px;top:307px">Red Rush</p>
    <p class="label sm" style="left:843px;top:307px">Lumen</p>
    <p class="label sm" style="left:1030px;top:307px">Frozen Espresso</p>
  </section>

  <section class="blended">
    <p class="label xxl" style="left:880px;top:478px">PureBlend Smoothies</p>
    <p class="label xl" style="left:880px;top:670px">Lemonade</p>
    <p class="label sm" style="left:718px;top:786px">Hot Chocolate</p>
    <p class="label sm" style="left:902px;top:786px">Italian Sodas</p>
    <p class="label sm" style="left:1053px;top:786px">Kids</p>
  </section>
</main>
</body>
</html>
```